Redesign of General Contractor Website

I currently have a wordpress site that needs some work. I would like to revitalize what we currently have to look more modern and up-to-date.
I want to be able to easily post pictures from new jobs and have a link to my own blog (not yet online). My current website can be found at www.drovanbuilders.com
the attached pictures are a site I built in Muse. i really like that sort of theme.
PLEASE NOTE: I am not interested in completely remaking the site, simply adding more functionalty and spicing it up a bit. (more animation, interactive elements, layering, etc...)
Target Market(s)
Property owners, Home owners, business owners, property managers, Decision makers purchasing a construction project, specifically Remodels, renovations, or damage restoration, with some or limited knowledge about how to complete one of those projects.
Industry/Entity Type
Contractor
Coding
Coded - Design and coding required
Number of Pages Required
1 page
Requirements
Must have
- Updateable photo bank displaying pictures from recent jobs that we can easily change and update. An embedded youtube pane showing our most recent video via our youtube channel. Animation and/or transition effects. The small circular logos must stay (I would like to see these be used with animation/transitional effects.
- Must be consistent with other marketing material. This can be found on our facebook page or in the power point file attached.
- Must use colors and fonts found at www.drovanbuilders.com
Nice to have
- Stock photos available if needed.
Should not have
- changes in logo design or re wording of text (use lorim ipsum if needed)
- No multiple pages, redesigning fonts

```html
<!DOCTYPE html>
<html lang="en">
<head>
<meta charset="utf-8">
<title>Drovan Builders — Home</title>
<link href="https://fonts.googleapis.com/css2?family=Roboto+Condensed:ital,wght@0,400;0,700;1,400;1,700&family=Permanent+Marker&display=swap" rel="stylesheet">
<style>
  :root {
    --brand-blue: #1f3a93;
    --brand-blue-dark: #172d75;
    --brand-orange: #f26a1b;
    --night-top: #3b4a86;
    --night-mid: #2a3468;
    --night-low: #111526;
    --ink-white: #ffffff;
    --ink-soft: #dfe4f5;
    --page-bg: #0b0b0b;
  }
  * { box-sizing: border-box; margin: 0; padding: 0; }
  html, body { width: 1078px; height: 1200px; overflow: hidden; background: var(--page-bg); }
  body { font-family: "Roboto Condensed", Arial, sans-serif; color: var(--ink-white); }

  .site { position: relative; width: 1078px; height: 1200px; overflow: hidden; }

  .hero-photo {
    position: absolute; inset: 0;
    background:
      radial-gradient(ellipse at 55% 30%, #55639f 0%, transparent 55%),
      linear-gradient(180deg, var(--night-top) 0%, var(--night-mid) 55%, var(--night-low) 82%, #05060b 100%);
  }

  .topbar {
    position: absolute; top: 0; left: 0; right: 0; height: 44px;
    background: var(--brand-blue);
    display: flex; justify-content: flex-end; align-items: center; gap: 34px;
    padding-right: 48px;
    font-style: italic; font-size: 14px; color: var(--ink-white);
  }
  .topbar .contact-item { display: flex; align-items: center; gap: 8px; }
  .topbar svg { width: 16px; height: 16px; }

  .logo-band {
    position: absolute; top: 150px; left: 0; width: 300px; height: 34px;
    background: var(--brand-blue);
  }
  .brand-badge {
    position: absolute; top: 104px; left: 70px;
    width: 126px; height: 126px; border-radius: 50%;
    background: var(--ink-white);
    display: flex; align-items: center; justify-content: center; text-align: center;
    box-shadow: 0 2px 10px rgba(0,0,0,.35);
  }
  .brand-badge .brand-name {
    font-weight: 700; font-size: 21px; line-height: 1.05; color: var(--brand-blue);
  }

  .main-nav {
    position: absolute; top: 66px; right: 48px;
    display: flex; gap: 56px; font-style: italic; font-size: 15px; text-transform: uppercase;
  }
  .main-nav a { color: var(--ink-white); text-decoration: none; position: relative; padding-top: 10px; }
  .main-nav a.is-active { color: var(--brand-orange); }
  .main-nav a.is-active::before {
    content: ""; position: absolute; top: 0; left: -4px; right: -4px; height: 3px; background: var(--brand-orange);
  }

  .hero-copy {
    position: absolute; top: 440px; left: 0; right: 0; text-align: center;
  }
  .hero-copy .lead {
    font-size: 54px; line-height: 1.05; font-weight: 400; text-transform: uppercase; letter-spacing: .5px;
  }
  .hero-copy .punch {
    font-family: "Permanent Marker", "Roboto Condensed", cursive;
    font-size: 118px; line-height: 1.1; color: var(--brand-orange); letter-spacing: 4px;
  }

  .hero-actions {
    position: absolute; top: 760px; left: 0; right: 0;
    display: flex; justify-content: center; gap: 18px;
  }
  .btn {
    display: flex; align-items: center; gap: 12px; height: 40px; padding: 0 18px;
    font-style: italic; font-size: 16px; text-transform: uppercase; text-decoration: none;
  }
  .btn svg { width: 16px; height: 16px; }
  .btn-primary { background: var(--brand-blue); color: var(--ink-white); }
  .btn-outline { border: 2px solid var(--brand-orange); color: var(--brand-orange); border-radius: 4px; font-weight: 700; }

  .slider-dots {
    position: absolute; top: 1150px; left: 0; right: 0;
    display: flex; justify-content: center; gap: 8px;
  }
  .slider-dots span { width: 9px; height: 9px; border-radius: 50%; background: var(--ink-soft); }
</style>
</head>
<body>
<div class="site">
  <div class="hero-photo" role="img" aria-label="Night photo of a lightning storm over a dark house silhouette with lit windows and trees"></div>

  <header>
    <div class="topbar">
      <span class="contact-item">1482 Alder Row, Kestrel Falls, TX 75011
        <svg viewBox="0 0 16 16" aria-hidden="true"><path d="M8 1 1 7.5h2V15h4v-4h2v4h4V7.5h2z" fill="#fff"/></svg>
      </span>
      <span class="contact-item">info@drovanbuilders.com
        <svg viewBox="0 0 16 16" aria-hidden="true"><rect x="1" y="3" width="14" height="10" fill="#fff"/><path d="M1 3l7 6 7-6" fill="none" stroke="#1f3a93" stroke-width="1.4"/></svg>
      </span>
      <span class="contact-item">(555) 014-2290
        <svg viewBox="0 0 16 16" aria-hidden="true"><circle cx="8" cy="8" r="7" fill="none" stroke="#fff" stroke-width="1.2"/><path d="M5.5 4.5l1.5 0 .6 2-1 .8a5 5 0 0 0 2.1 2.1l.8-1 2 .6v1.5c-3.5.4-6.4-2.5-6-6z" fill="#fff"/></svg>
      </span>
    </div>

    <div class="logo-band"></div>
    <div class="brand-badge"><span class="brand-name">Drovan<br>Builders</span></div>

    <nav class="main-nav">
      <a href="#" class="is-active">Home</a>
      <a href="#">About Us</a>
      <a href="#">Services</a>
      <a href="#">Portfolio</a>
      <a href="#">Testimonials</a>
      <a href="#">Contact</a>
    </nav>
  </header>

  <main>
    <div class="hero-copy">
      <p class="lead">The latest storm have<br>you feeling a little</p>
      <p class="punch">EXPOSE?</p>
    </div>

    <div class="hero-actions">
      <a href="#" class="btn btn-primary">Contact Us
        <svg viewBox="0 0 16 16" aria-hidden="true"><ellipse cx="6.5" cy="6.5" rx="5.5" ry="4.5" fill="#fff"/><ellipse cx="10" cy="10" rx="5" ry="4" fill="none" stroke="#fff" stroke-width="1.2"/></svg>
      </a>
      <a href="#" class="btn btn-outline">Watch Video
        <svg viewBox="0 0 16 16" aria-hidden="true"><rect x="1" y="3" width="14" height="10" rx="2" fill="#f26a1b"/><path d="M6.5 5.5v5l4-2.5z" fill="#172d75"/></svg>
      </a>
    </div>

    <div class="slider-dots"><span></span><span></span><span></span><span></span></div>
  </main>
</div>
</body>
</html>
```